Business Card Design

I need a business card design for my law office based in Pasadena, California. I am a sole practitioner and I specialize in business transaction and litigation, probate and estate planning, taxation law, corporate and business formation, immigration and real estate. I want something that is simple, yet stands out.

A friend helped to create a logo about 6 years ago. I am open to new ideas to changing the logo.

Industry/Entity Type

Business

Contact Information for Business Card

Law Offices of Dorvan L. Mabry
842 W. Larkspur Ave., Suite 319
Pasadena, CA 90287
Tel: 626-555-0174
Fax: 626-555-0139
Email: dmabry@dlmlegalgroup.example

Attorney: Dorvan L. Mabry

```html
<!DOCTYPE html>
<html lang="en">
<head>
<meta charset="utf-8">
<title>Business Card – Law Offices of Dorvan L. Mabry</title>
<link href="https://fonts.googleapis.com/css2?family=Open+Sans:wght@400;600&display=swap" rel="stylesheet">
<style>
  :root {
    --backdrop: #dcdcdc;
    --card: #f7f7f7;
    --brand-brown: #5b3a1e;
    --brand-copper: #c67b37;
    --text-grey: #555555;
    --text-dark: #3a3a3a;
  }
  * { box-sizing: border-box; margin: 0; padding: 0; }
  html, body {
    width: 1200px;
    height: 750px;
    overflow: hidden;
    background: var(--backdrop);
    font-family: "Open Sans", sans-serif;
  }
  .sheet {
    position: relative;
    width: 1200px;
    height: 750px;
  }
  .card {
    position: absolute;
    width: 540px;
    height: 309px;
    background: var(--card);
    border-radius: 24px;
    box-shadow: 0 3px 10px rgba(0,0,0,0.12);
  }
  .card--front { left: 40px; top: 130px; }
  .card--back  { left: 620px; top: 310px; }

  .wordmark {
    display: flex;
    align-items: center;
    gap: 12px;
    color: var(--brand-brown);
    font-weight: 600;
  }
  .wordmark__square {
    background: var(--brand-copper);
    flex: none;
  }
  .wordmark__name { line-height: 1.25; }

  .card--front .wordmark {
    position: absolute;
    left: 0; right: 0; top: 0; bottom: 0;
    justify-content: center;
    font-size: 24px;
  }
  .card--front .wordmark__square { width: 40px; height: 40px; }

  .card--back .wordmark {
    position: absolute;
    right: 34px;
    top: 40px;
    font-size: 13px;
    gap: 8px;
  }
  .card--back .wordmark__square { width: 20px; height: 20px; }

  .contact {
    position: absolute;
    left: 44px;
    bottom: 34px;
  }
  .contact__name {
    color: var(--brand-copper);
    font-size: 19px;
    font-weight: 400;
    line-height: 1.1;
  }
  .contact__role {
    color: var(--text-grey);
    font-size: 13px;
    margin-top: 2px;
    margin-bottom: 14px;
  }
  .contact__line {
    color: var(--text-dark);
    font-size: 14px;
    line-height: 1.32;
  }
</style>
</head>
<body>
  <main class="sheet">
    <section class="card card--front" aria-label="Card front">
      <div class="wordmark">
        <span class="wordmark__square"></span>
        <span class="wordmark__name">Law Offices of Dorvan L. Mabry</span>
      </div>
    </section>

    <section class="card card--back" aria-label="Card back">
      <div class="wordmark">
        <span class="wordmark__square"></span>
        <span class="wordmark__name">Law Offices of<br>Dorvan L. Mabry</span>
      </div>
      <div class="contact">
        <p class="contact__name">Dorvan L. Mabry</p>
        <p class="contact__role">Attorney</p>
        <p class="contact__line">626-555-0174</p>
        <p class="contact__line">626-555-0139</p>
        <p class="contact__line">dmabry@dlmlegalgroup.example</p>
        <p class="contact__line">842 W. Larkspur Ave., Suite 319</p>
        <p class="contact__line">Pasadena, CA 90287</p>
      </div>
    </section>
  </main>
</body>
</html>
```